ORVILMA card Technical Architecture

Hello everyone ORVILMA: It is a consulting firm in Architecture and Construction. I require a card duplexing, sober, elegant, classic but not boring. Update 1: Use the following data for the card. Name: Rodrigo Salinas Tomás Quevedo Position: COO Twitter: @orvilmaAT Homepage: orvilma.com home address not include the participation of all thank you.

Target Market(s)

Construction companies, Architects and Consulting Engineers

Industry/Entity Type

Consulting

Contact Information for Business Card

Los campos que debe tener:
Nombre, Cargo, email, homepage y twitter

Font styles to use
Serif
Sans Serif
Other font styles liked:
• Me gustan playfair display, open sans y roboto, pero estoy sujeto a sus propuestas

Requirements
Must have
• Colors: Present combined proposals in white, red, gray and black Update 1: The two names must be clearly differentiated from the two surnames
Nice to have
• They are free to present their best proposals. I will bring them immediate feedback to the extent you can go see their designs. Complete data for card and logo files will give the winner the

```html
<!DOCTYPE html>
<html lang="es">
<head>
<meta charset="utf-8">
<title>ORVILMA – Business Card</title>
<link href="https://fonts.googleapis.com/css2?family=Roboto:wght@300;500&display=swap" rel="stylesheet">
<style>
  :root {
    --page-bg: #8a8a8a;
    --card-black: #050505;
    --deep-red: #420000;
    --mid-red: #2a0000;
    --accent-red: #d8323c;
    --white: #ffffff;
  }
  * { margin: 0; padding: 0; box-sizing: border-box; }
  html, body {
    width: 1200px;
    height: 1200px;
    overflow: hidden;
    background: var(--page-bg);
    font-family: "Roboto", sans-serif;
  }
  .card {
    position: absolute;
    left: 226px;
    width: 752px;
    height: 426px;
    border-radius: 22px;
    overflow: hidden;
  }
  .card--front {
    top: 126px;
    background: radial-gradient(ellipse 62% 78% at 50% 48%, #000 0%, #120000 35%, var(--mid-red) 60%, var(--deep-red) 82%);
  }
  .front-mark {
    position: absolute;
    left: 254px;
    top: 82px;
    width: 220px;
    height: 212px;
    background: var(--card-black);
    display: flex;
    align-items: center;
    justify-content: center;
  }
  .front-mark__name {
    color: var(--accent-red);
    font-weight: 500;
    font-size: 30px;
    letter-spacing: 4px;
  }
  .card--back {
    top: 618px;
    background: linear-gradient(180deg, var(--card-black) 0%, var(--card-black) 42%, #150000 70%, var(--mid-red) 100%);
  }
  .brand {
    position: absolute;
    right: 24px;
    top: 104px;
    text-align: right;
  }
  .brand__name {
    color: var(--white);
    font-weight: 300;
    font-size: 36px;
    letter-spacing: 15px;
    line-height: 1;
    margin-right: -15px;
  }
  .brand__tagline {
    margin-top: 10px;
    padding-top: 4px;
    border-top: 1px solid #3a0a0a;
    color: var(--accent-red);
    font-size: 11.5px;
    letter-spacing: 4.6px;
    margin-right: -4.6px;
  }
  .person {
    position: absolute;
    left: 30px;
    top: 240px;
  }
  .person__name {
    color: var(--white);
    font-weight: 500;
    font-size: 29px;
    letter-spacing: -0.2px;
    line-height: 1.1;
  }
  .person__role {
    color: var(--accent-red);
    font-weight: 300;
    font-size: 19px;
    line-height: 1.2;
  }
  .contacts {
    list-style: none;
    margin-top: 26px;
  }
  .contacts__item {
    display: flex;
    align-items: center;
    gap: 7px;
    color: var(--white);
    font-weight: 300;
    font-size: 21px;
    line-height: 25.5px;
  }
  .contacts__icon { width: 15px; height: 15px; flex: none; }
</style>
</head>
<body>
  <section class="card card--front" aria-label="Card front">
    <div class="front-mark">
      <span class="front-mark__name">ORVILMA</span>
    </div>
  </section>

  <section class="card card--back" aria-label="Card back">
    <div class="brand">
      <div class="brand__name">ORVILMA</div>
      <div class="brand__tagline">ARQUITECTURA TÉCNICA</div>
    </div>

    <div class="person">
      <h1 class="person__name">Rodrigo Salinas Tomás Quevedo</h1>
      <p class="person__role">COO</p>
      <ul class="contacts">
        <li class="contacts__item">
          <svg class="contacts__icon" viewBox="0 0 16 16" aria-hidden="true">
            <rect x="1" y="3" width="14" height="10" fill="#d8323c"/>
            <path d="M1 3 L8 9 L15 3" fill="none" stroke="#050505" stroke-width="1.3"/>
          </svg>
          rodrigo@orvilma.com
        </li>
        <li class="contacts__item">
          <svg class="contacts__icon" viewBox="0 0 16 16" aria-hidden="true" fill="none" stroke="#d8323c" stroke-width="1.2">
            <circle cx="8" cy="8" r="6.5"/>
            <ellipse cx="8" cy="8" rx="3" ry="6.5"/>
            <path d="M1.5 8 H14.5 M2.5 4.8 H13.5 M2.5 11.2 H13.5"/>
          </svg>
          orvilma.com
        </li>
        <li class="contacts__item">
          <svg class="contacts__icon" viewBox="0 0 16 16" aria-hidden="true">
            <rect x="1.5" y="1.5" width="13" height="13" rx="1.5" fill="#d8323c"/>
          </svg>
          @orvilmaAT
        </li>
      </ul>
    </div>
  </section>
</body>
</html>
```